Funeral Home needs a tri-fold brochure

We need to have a tri-fold brochure designed for our mortuary. The name of the mortuary is Willowmere Mortuary. The purpose of this brochure is to give consumers and decision makers an easy glimpse into our business.

The brochure will be tri-fold and have full color on both side.(8.5 x 11)

We are not what most people think in terms of a "traditional" funeral home. Do not use anything with a gothic feel. Our logo is light and simple which is how we would like this brochure to also be. The logo is attached. The colors we like are green, gold, white, and black.

Our mortuary offers affordable burial and cremation services. Some key points that we would like noted in brochure are family owned and operated, on-site cremation, and we service all religious faiths.

This is my first time requesting a brochure with ArtFolio, so I'm not sure if I should have text already written or not. I'm open to any questions or suggestions so don't be afraid to ask. I will answer as soon as possible.
Updates

I have just uploaded a scan of an old brochure that the business used that we don't want the new one to look anything like. Also I uploaded a sheet of copy for the features we would like shown on the brochure. Added Wednesday, September 10, 2014

Target Market(s)

decision influencers in churches, hospices, and hospitals. Also families that may be in need of our service.

Industry/Entity Type

Funeral Home

Font styles to use
Serif

Colors
acd036

Requirements
Must have
• My project must have our logo and be a bright brochure.
Should not have
• The project should not have a gothic feel, or use anything that is associated with "traditional" mortuaries like the dove or horse and carriage. No pictures of caskets, urns, or hearses. I have attached a picture of an older brochure that the business has. New design should not look anything like this one.

```html
<!DOCTYPE html>
<html lang="en">
<head>
<meta charset="utf-8">
<title>Willowmere Mortuary – Tri-fold Brochure</title>
<link rel="stylesheet" href="https://fonts.googleapis.com/css2?family=Open+Sans:ital,wght@0,400;0,600;0,700;0,800;1,600;1,700&display=swap">
<style>
  :root {
    --green: #8cc63f;
    --lime: #acd036;
    --green-dark: #5c9a1f;
    --gold: #f5e34d;
    --white: #ffffff;
    --paper: #f7f7f5;
    --ink: #1a1a1a;
    --backdrop: #e4e4e4;
  }
  * { box-sizing: border-box; margin: 0; padding: 0; }
  html, body { width: 1033px; height: 1200px; overflow: hidden; }
  body { background: var(--backdrop); font-family: "Open Sans", Arial, sans-serif; color: var(--ink); position: relative; }

  .sheet { position: absolute; left: 154px; width: 725px; height: 560px; background: var(--paper); overflow: hidden; box-shadow: 0 4px 14px rgba(0,0,0,.18); }
  .sheet--outside { top: 27px; }
  .sheet--inside { top: 613px; }
  .panel { position: absolute; top: 0; width: 241.67px; height: 560px; }
  .panel--1 { left: 0; } .panel--2 { left: 241.67px; } .panel--3 { left: 483.33px; }
  .art { position: absolute; left: 0; top: 0; }

  /* Outside: pricing panel */
  .pricing { background: var(--green); color: var(--white); text-align: center; padding: 18px 14px 0; }
  .price-item { margin-bottom: 9px; }
  .price-item h3 { font-size: 11px; font-weight: 600; line-height: 1.3; }
  .price-item .price { color: var(--gold); font-size: 11px; font-weight: 700; line-height: 1.3; }
  .price-item p { font-size: 7.8px; font-weight: 600; line-height: 1.3; margin-top: 2px; }
  .price-item p .lead { color: var(--gold); }
  .rule { width: 90px; height: 1px; background: var(--gold); opacity: .8; margin: 7px auto 0; }

  /* Outside: contact + cover */
  .cover-title { position: absolute; left: 420px; top: 22px; padding-left: 8px; border-left: 1.5px solid var(--white); color: var(--white); font-size: 19px; line-height: 1.28; font-weight: 400; }
  .contact { position: absolute; left: 14px; top: 458px; font-size: 9px; font-weight: 600; line-height: 1.4; }
  .contact-row { display: flex; align-items: flex-start; gap: 5px; margin-bottom: 8px; }
  .contact-row svg { flex: none; margin-top: 2px; }
  .contact-list .contact-row { margin-bottom: 1px; align-items: center; }
  .contact-list .contact-row svg { margin-top: 0; }
  .brand { display: flex; align-items: center; gap: 9px; color: var(--ink); font-weight: 800; }
  .brand-dot { border-radius: 50%; background: var(--lime); flex: none; }
  .brand-name { line-height: 1; text-transform: uppercase; }
  .brand--cover { position: absolute; left: 503px; top: 482px; }
  .brand--cover .brand-dot { width: 24px; height: 24px; }
  .brand--cover .brand-name { font-size: 17px; }
  .cover-web { position: absolute; left: 0; width: 241.67px; top: 532px; text-align: center; font-size: 12px; font-weight: 700; }

  /* Inside */
  .about { position: absolute; left: 22px; top: 26px; width: 430px; color: var(--white); font-size: 11.5px; font-weight: 700; font-style: italic; line-height: 1.3; }
  .about p + p { margin-top: 10px; }
  .brand--inside { position: absolute; left: 22px; top: 252px; }
  .brand--inside .brand-dot { width: 30px; height: 30px; }
  .brand--inside .brand-name { font-size: 18px; }
  .features { position: absolute; left: 0; top: 315px; width: 241.67px; text-align: center; color: var(--lime); font-style: italic; font-weight: 700; font-size: 12px; }
  .features li { list-style: none; margin-bottom: 40px; line-height: 1.2; }
  .features li small { display: block; font-size: 9px; font-weight: 600; }
  .services-tag { position: absolute; left: 284px; top: 252px; background: var(--lime); color: var(--white); font-size: 10px; font-weight: 700; font-style: italic; letter-spacing: .5px; padding: 1px 14px; border-radius: 4px; }
  .brand--small { position: absolute; left: 284px; top: 270px; }
  .brand--small .brand-dot { width: 14px; height: 14px; }
  .brand--small .brand-name { font-size: 10px; }
  .services { position: absolute; left: 270px; top: 305px; width: 205px; color: var(--green); font-style: italic; font-weight: 700; font-size: 12px; }
  .services li { list-style: none; display: flex; gap: 8px; margin-bottom: 22px; line-height: 1.15; }
  .services li svg { flex: none; margin-top: 2px; }
  .services li small { display: block; font-size: 9px; font-weight: 600; }
  .web-pill { position: absolute; left: 300px; top: 520px; background: var(--lime); color: var(--white); font-size: 9.5px; font-weight: 700; padding: 4px 12px; border-radius: 3px; white-space: nowrap; }
  .faith-tag { position: absolute; left: 500px; top: 222px; background: var(--lime); color: var(--white); font-size: 12px; font-weight: 700; letter-spacing: .6px; padding: 2px 14px; border-radius: 3px; }
  .faiths { position: absolute; left: 483px; top: 248px; width: 241.67px; text-align: center; color: var(--green); font-size: 9.5px; font-weight: 700; line-height: 1.3; }
  .family-photo { position: absolute; left: 520px; top: 320px; width: 205px; height: 240px; border-radius: 60% 0 0 0 / 40% 0 0 0; background: radial-gradient(ellipse at 55% 45%, #d9b585 0%, #8a6a4a 35%, #3a2c24 70%, #f0f3dc 100%); }
</style>
</head>
<body>

<section class="sheet sheet--outside" aria-label="Brochure outside">
  <div class="panel panel--1 pricing">
    <div class="price-item">
      <h3>Direct Non-Ceremonial Cremation</h3>
      <div class="price">$ 745</div>
      <p><span class="lead">Simple Cremation with basic professional services:</span> Our professional services, Transfer of your loved one into our care, Alternative Cremation Container, Cremation, Basic Plastic Urn, and Web page Obituary.</p>
      <div class="rule"></div>
    </div>
    <div class="price-item">
      <h3>Memorial Cremation Packages</h3>
      <div class="price">$ 1,295 to 1,820</div>
      <p>Service directed by our professional staff at our facility or a different venue of choice and also includes an Immediate Family (spouse, children, parents) Viewing at our facility prior to cremation. Our professional services, Transfer of your loved one into our care, Memorial Services, Printed Memorial Package, Cremation, Merchandise Allowance.</p>
      <div class="rule"></div>
    </div>
    <div class="price-item">
      <h3>Traditional Cremation Packages</h3>
      <div class="price">$2,180 to 2,555</div>
      <p>Traditional Funeral with a viewing and then Cremation to follow. Directed by our professional staff, the funeral venue can be our beautiful facilities, a familiar place of worship, or any place of healing. Transfer of your loved one into our care, Embalming, Viewing and Funeral Preparation, Funeral Services, Printed Memorial Package, Merchandise Allowance, Cremation, Web page Obituary</p>
      <div class="rule"></div>
    </div>
    <div class="price-item">
      <h3>Tradition Burial Packages</h3>
      <div class="price">$3,100 to 5,300</div>
      <p>Tradition Funeral with viewing and then burial. Directed by our professional staff, the funeral venue can be our beautiful facilities, a familiar place of worship, or any place of healing and then transfer to the cemetery. Transfer of your loved one into our care, Embalming, Viewing and Funeral Preparation, Funeral Services, Printed Memorial Package, Merchandise Allowance for Casket, Transfer to cemetery and committal service, Web page Obituary.</p>
    </div>
  </div>

  <svg class="art" width="725" height="560" viewBox="0 0 725 560">
    <defs>
      <linearGradient id="gardenTones" x1="0" y1="0" x2="1" y2="1">
        <stop offset="0" stop-color="#5e7f3a"/>
        <stop offset=".5" stop-color="#3f5a2a"/>
        <stop offset="1" stop-color="#7fa04a"/>
      </linearGradient>
    </defs>
    <path d="M400 475 C 470 478, 570 445, 725 405 L725 440 C 590 468, 480 488, 400 475 Z" fill="var(--lime)"/>
    <path d="M300 0 C 250 150, 260 400, 400 475 C 470 478, 570 445, 725 410 L725 0 Z" fill="url(#gardenTones)" role="img" aria-label="Photo of a woman comforting an elderly man in a sunlit garden"/>
    <path d="M300 0 C 250 150, 260 400, 400 475" fill="none" stroke="var(--lime)" stroke-width="6"/>
  </svg>

  <div class="cover-title">Affordable<br>Cremation<br>and Burial</div>

  <div class="panel panel--2">
    <div class="contact">
      <div class="contact-row">
        <svg width="9" height="12" viewBox="0 0 9 12"><path d="M4.5 0A4.5 4.5 0 0 0 0 4.5C0 8 4.5 12 4.5 12S9 8 9 4.5A4.5 4.5 0 0 0 4.5 0Z" fill="var(--green)"/><circle cx="4.5" cy="4.5" r="1.7" fill="var(--white)"/></svg>
        <span>4120 W. Meadowlark Rd,<br>Sun Vale, AZ 85000</span>
      </div>
      <div class="contact-list">
        <div class="contact-row"><svg width="10" height="10" viewBox="0 0 10 10"><path d="M2 0h2l1 3-1.5 1a6 6 0 0 0 2.5 2.5L7 5l3 1v2a2 2 0 0 1-2 2A8 8 0 0 1 0 2a2 2 0 0 1 2-2Z" fill="var(--green)"/></svg><span>555-210-4400</span></div>
        <div class="contact-row"><svg width="10" height="10" viewBox="0 0 10 10"><rect x="0" y="3" width="10" height="6" rx="1" fill="var(--green)"/><rect x="2" y="0" width="6" height="3" fill="var(--green)"/></svg><span>555-210-4401</span></div>
        <div class="contact-row"><svg width="10" height="8" viewBox="0 0 10 8"><rect width="10" height="8" rx="1" fill="var(--green)"/><path d="M0 0l5 4 5-4" fill="none" stroke="var(--white)" stroke-width="1"/></svg><span>wecare@willowmeremortuary.com</span></div>
      </div>
    </div>
  </div>

  <div class="brand brand--cover"><span class="brand-dot"></span><span class="brand-name">Willowmere<br>Mortuary</span></div>
  <div class="panel panel--3"><div class="cover-web">www.WillowmereMortuary.com</div></div>
</section>

<section class="sheet sheet--inside" aria-label="Brochure inside">
  <svg class="art" width="725" height="560" viewBox="0 0 725 560">
    <defs>
      <linearGradient id="lawnTones" x1="0" y1="0" x2="0" y2="1">
        <stop offset="0" stop-color="#9fb8cf"/>
        <stop offset=".45" stop-color="#4f6b3a"/>
        <stop offset=".6" stop-color="#7fa347"/>
        <stop offset="1" stop-color="#6e9a2e"/>
      </linearGradient>
    </defs>
    <path d="M0 0H725V185C 620 200, 540 220, 470 215 L0 190 Z" fill="var(--green)"/>
    <path d="M0 190 C 200 205, 380 220, 470 215 C 420 225, 200 215, 0 212 Z" fill="var(--lime)"/>
    <path d="M545 0 C 480 60, 470 160, 520 205 C 600 200, 660 190, 725 175 L725 0 Z" fill="url(#lawnTones)" role="img" aria-label="Photo of the mortuary building behind a green lawn and old trees"/>
    <path d="M545 0 C 480 60, 470 160, 520 205" fill="none" stroke="var(--lime)" stroke-width="6"/>
  </svg>

  <div class="about">
    <p>Willowmere Mortuary was started in 2001 with the goal of providing an affordable burial and cremation service without cutting corners.</p>
    <p>Now owned by father and son duo, Daniel and Thomas Harlow, Willowmere Mortuary is proud to be family owned and operated and a leader in the funeral industry.</p>
  </div>

  <div class="brand brand--inside"><span class="brand-dot"></span><span class="brand-name">Willowmere<br>Mortuary</span></div>
  <ul class="features">
    <li>Affordable services</li>
    <li>On-site Crematory<small>(loved one never leaves our care)</small></li>
    <li>In-House financing available</li>
  </ul>

  <div class="services-tag">SERVICES</div>
  <div class="brand brand--small"><span class="brand-dot"></span><span class="brand-name">Willowmere<br>Mortuary</span></div>
  <ul class="services">
    <li><svg width="14" height="14" viewBox="0 0 14 14"><circle cx="7" cy="7" r="7" fill="var(--lime)"/><path d="M3.5 7.2l2.3 2.3 4.7-5" fill="none" stroke="var(--white)" stroke-width="1.6"/></svg><span>Cremation services<small>(immediate or with a service)</small></span></li>
    <li><svg width="14" height="14" viewBox="0 0 14 14"><circle cx="7" cy="7" r="7" fill="var(--lime)"/><path d="M3.5 7.2l2.3 2.3 4.7-5" fill="none" stroke="var(--white)" stroke-width="1.6"/></svg><span>Burial Services</span></li>
    <li><svg width="14" height="14" viewBox="0 0 14 14"><circle cx="7" cy="7" r="7" fill="var(--lime)"/><path d="M3.5 7.2l2.3 2.3 4.7-5" fill="none" stroke="var(--white)" stroke-width="1.6"/></svg><span>Transportation out of state<small>(ship out)</small></span></li>
  </ul>
  <div class="web-pill">www.WillowmereMortuary.com</div>

  <div class="faith-tag">Serves all faiths</div>
  <div class="faiths">Catholic, Protestant<br>LDS, Hindu, Buddhist<br>Non-denominational</div>
  <div class="family-photo" role="img" aria-label="Photo of a mother embracing her child"></div>
</section>

</body>
</html>
```